Bright acorns day nursery pkr limited

we would like create a website that can be updated by us easily as we have regular changes to what we provide and need. we would like something that is classy but also appealing from a child's aspect. we would be looking to add our own logo and our edvarn logo both attached, if you guys can create it and we will work with the preferred choice to add all the text.
We would like the links to nest ledger, edvarn report and our chatterly feed on the front page

we are looking for a website for our childcare business we have 2 nurseries that we would like one website.
showing our opening hours, price list, policies etc as well as photos, description of our day, staff photos and their training accreditation's.

Target Market(s)

Families

Industry/Entity Type

Childcare

Number of Pages Required

5+ page

Font styles to use
Serif

Colors

Designer to choose colors to be used in the design.

Requirements
Must have
• links to social media and other websites, photographs, links to download registration forms etc, parents able to leave reviews. zarloo charts link, job opportunities
Nice to have
• facilities to take payments

```html
<!DOCTYPE html>
<html lang="en">
<head>
<meta charset="utf-8">
<title>Bright Acorns Day Nursery</title>
<link rel="stylesheet" href="https://fonts.googleapis.com/css2?family=Patrick+Hand&family=Open+Sans:wght@400;600;700&display=swap">
<style>
:root{
  --green:#2f8a2f;
  --magenta:#c2127a;
  --navy:#0d2a66;
  --ink:#1a1a2e;
  --heading:#1b2a6b;
  --text:#555;
  --light:#f3f3f3;
  --footer:#121212;
  --footer-bar:#0a0a0a;
  --white:#fff;
}
*{box-sizing:border-box;margin:0;padding:0}
html,body{width:1200px;height:4467px;overflow:hidden}
body{position:relative;font-family:"Open Sans",sans-serif;color:var(--text);background:var(--white)}
.abs{position:absolute}
.hand{font-family:"Patrick Hand",cursive;letter-spacing:1px}
.btn{position:absolute;display:flex;align-items:center;justify-content:center;border:2px solid var(--white);color:var(--white);font-weight:700;font-size:14px;border-radius:6px;letter-spacing:.5px}

.site-header{position:absolute;left:0;top:0;width:1200px;height:80px;background:var(--white);z-index:3}
.logo{position:absolute;left:92px;top:6px;width:170px;height:170px;border-radius:50%;background:var(--white);box-shadow:0 2px 8px rgba(0,0,0,.15);display:flex;align-items:center;justify-content:center;text-align:center;z-index:4}
.logo span{font-family:"Patrick Hand",cursive;font-size:26px;line-height:1.05;color:var(--heading);width:130px}
.nav{position:absolute;left:534px;top:32px;display:flex;gap:38px;font-weight:700;font-size:14px;color:#222}
.search{position:absolute;left:1064px;top:22px;width:34px;height:34px;border-radius:50%;background:var(--green)}

.hero{position:absolute;left:0;top:80px;width:1200px;height:581px;background:linear-gradient(120deg,#6d5a4a 0%,#b59b86 40%,#d9c7b6 70%,#8f7a68 100%)}
.hero-title{position:absolute;left:0;width:1200px;top:185px;text-align:center;color:var(--white);font-size:52px;font-weight:400;font-style:italic}
.hero-sub{position:absolute;left:0;width:1200px;top:262px;text-align:center;color:var(--white);font-size:28px}
.slider-arrow{position:absolute;top:290px;width:30px;height:30px;border-radius:50%;background:rgba(0,0,0,.35)}

.welcome{position:absolute;left:0;top:661px;width:1200px;height:301px;background:var(--green)}
.section-title{position:absolute;left:0;width:1200px;text-align:center;font-size:34px;font-weight:400}
.welcome p{position:absolute;left:240px;width:720px;top:105px;text-align:center;color:var(--white);font-size:12.5px;line-height:22px}

.services-title{color:var(--heading);font-style:italic}
.subtitle{position:absolute;left:0;width:1200px;text-align:center;font-size:14px;color:var(--text)}
.service{position:absolute;width:300px}
.service h3{font-family:"Patrick Hand",cursive;font-size:24px;font-weight:400;color:var(--ink);letter-spacing:1px;font-style:italic}
.service p{font-size:12.5px;line-height:20px;color:var(--text)}
.service.left{text-align:right}
.svc-icon{position:absolute;width:54px;height:54px;border-radius:50%;background:var(--magenta);display:flex;align-items:center;justify-content:center}

.learning{position:absolute;left:0;top:1638px;width:1200px;height:342px;background:linear-gradient(90deg,#2b2420,#4a3d36 50%,#2b2420)}
.learning p{position:absolute;left:220px;width:760px;top:140px;text-align:center;color:var(--white);font-size:12.5px;line-height:22px}

.price-card{position:absolute;top:2138px;width:235px;height:372px;background:var(--white);border-radius:10px;box-shadow:0 2px 10px rgba(0,0,0,.18);overflow:hidden}
.price-head{position:absolute;left:0;top:0;width:235px;height:140px}
.price-head h3{position:absolute;left:0;width:235px;top:22px;text-align:center;color:var(--white);font-size:26px;font-weight:400}
.price-head small{position:absolute;left:0;width:235px;top:64px;text-align:center;color:var(--white);font-weight:700;font-size:13px}
.perks{position:absolute;left:52px;top:150px;font-size:11.5px;line-height:23px;color:#333}
.perks li{list-style:none;display:flex;align-items:center;gap:6px}
.age{position:absolute;top:215px;font-size:14px;font-weight:700;color:var(--magenta)}
.pill{position:absolute;top:246px;width:68px;height:28px;border-radius:6px;background:var(--navy);color:var(--white);font-weight:700;font-size:14px;display:flex;align-items:center;justify-content:center}
.view{position:absolute;left:56px;top:305px;width:123px;height:36px;border-radius:5px;background:var(--green);color:var(--white);font-weight:700;font-size:13px;display:flex;align-items:center;justify-content:center}

.day{position:absolute;left:0;top:2606px;width:1200px;height:342px;background:var(--navy)}
.day h2{position:absolute;left:98px;top:70px;color:var(--white);font-size:38px;font-style:italic;font-weight:400}
.day p{position:absolute;left:98px;top:135px;width:580px;color:var(--white);font-size:12.5px;line-height:24px}
.day-image{position:absolute;left:700px;top:0;width:500px;height:342px;background:radial-gradient(ellipse at 62% 58%,#f2c4b8 0%,#e8a0b0 28%,#5d86c7 58%,var(--navy) 78%)}

.teacher{position:absolute;top:3151px;width:235px;height:327px;border-radius:118px 118px 14px 14px;background:var(--white);box-shadow:0 2px 10px rgba(0,0,0,.18)}
.teacher .photo{position:absolute;left:18px;top:16px;width:199px;height:199px;border-radius:50%;border:4px solid #f0f0f0}
.teacher h4{position:absolute;left:0;width:235px;top:230px;text-align:center;font-size:15px;font-weight:600;color:#222}
.teacher .role{position:absolute;left:0;width:235px;top:254px;text-align:center;font-size:13px;color:var(--text)}
.socials{position:absolute;left:0;width:235px;top:285px;display:flex;justify-content:center;gap:12px}
.socials span{width:26px;height:26px;border-radius:50%;border:1.5px solid var(--magenta);display:flex;align-items:center;justify-content:center}
.side-arrow{position:absolute;top:3296px}

.accred{position:absolute;left:0;top:3574px;width:1200px;height:363px;background:var(--light)}
.badge-box{position:absolute;top:172px;width:190px;height:116px;background:var(--white);border:1px solid #ddd;display:flex;align-items:center;justify-content:center;gap:10px}

.footer{position:absolute;left:0;top:3937px;width:1200px;height:435px;background:var(--footer);color:var(--white)}
.footer h5{position:absolute;top:86px;font-size:15px;font-weight:600;letter-spacing:.5px}
.contact-item{position:absolute;left:98px;display:flex;align-items:center;gap:18px;font-size:12px;line-height:19px}
.contact-item .ic{width:38px;height:38px;border-radius:50%;border:1.5px solid var(--white);flex:none;display:flex;align-items:center;justify-content:center}
.news-input{position:absolute;left:417px;top:138px;width:226px;height:37px;border:1px solid #888;font-size:12px;padding:10px;color:#ddd}
.subscribe{position:absolute;left:417px;top:186px;width:100px;height:34px;background:var(--magenta);font-size:12px;font-weight:600;display:flex;align-items:center;justify-content:center}
.seal{position:absolute;border-radius:4px}
.feed{position:absolute;left:747px;top:137px;width:352px;height:232px;background:var(--white);color:#222}
.feed-banner{position:absolute;left:0;top:0;width:352px;height:110px;background:linear-gradient(120deg,#6b7b94,#3a4558)}
.feed-banner b{position:absolute;left:94px;top:14px;color:var(--white);font-size:13px}
.feed-banner small{position:absolute;left:94px;top:34px;color:var(--white);font-size:11px}
.feed-logo{position:absolute;left:12px;top:12px;width:70px;height:70px;background:var(--white)}
.bottom-bar{position:absolute;left:0;top:4372px;width:1200px;height:95px;background:var(--footer-bar);color:#ccc;font-size:12px}
</style>
</head>
<body>

<header class="site-header">
  <nav class="nav"><span>HOME</span><span>ABOUT US</span><span>PAGES</span><span>GALLERY</span><span>CONTACT US</span></nav>
  <div class="search"><svg width="34" height="34" viewBox="0 0 34 34"><circle cx="15.5" cy="15.5" r="5.5" fill="none" stroke="#fff" stroke-width="2"/><line x1="19.5" y1="19.5" x2="23" y2="23" stroke="#fff" stroke-width="2.2"/></svg></div>
</header>
<div class="logo"><span>Bright Acorns Day Nursery</span></div>

<section class="hero" role="img" aria-label="Photo of a carer playing with a toddler and a bead-maze toy">
  <h1 class="hero-title hand">BRIGHT ACORNS DAY NURSERY</h1>
  <p class="hero-sub">Lorem Ipsum is simply dummy text of the printing</p>
  <div class="btn" style="left:534px;top:362px;width:132px;height:42px;">JOIN NOW!</div>
  <div class="slider-arrow" style="left:32px"><svg width="30" height="30"><path d="M18 9l-6 6 6 6" stroke="#fff" stroke-width="2" fill="none"/></svg></div>
  <div class="slider-arrow" style="left:1138px"><svg width="30" height="30"><path d="M12 9l6 6-6 6" stroke="#fff" stroke-width="2" fill="none"/></svg></div>
</section>

<section class="welcome">
  <h2 class="section-title hand" style="top:42px;color:#fff;font-style:italic">WELCOME TO BRIGHT ACORNS DAY NURSERY</h2>
  <p>There are many variations of passages of Lorem Ipsum available, but the majority have suffered alteration in some form, by injected humour, or randomised words which don't look even slightly believable. If you are going to use a passage of Lorem Ipsum, you need to be sure there isn't anything embarrassing hidden in the middle of text.</p>
  <div class="btn" style="left:538px;top:210px;width:124px;height:40px;">READ MORE</div>
</section>

<section>
  <h2 class="section-title hand services-title" style="top:1044px">OUR SERVICES</h2>
  <p class="subtitle" style="top:1088px">We provide the best services to your child</p>
  <div class="abs" role="img" aria-label="Photo of two toddlers in striped outfits playing with toys" style="left:450px;top:1176px;width:354px;height:314px;border-radius:50%;background:radial-gradient(circle,#e9d3cc 0%,#d9c2bb 35%,#f1e6e2 58%,#fff 72%)"></div>

  <div class="service left" style="left:80px;top:1178px"><h3>MANY SPORTS</h3><p>It is a long established fact that a reader<br>will be distracted by the readable</p></div>
  <div class="svc-icon" style="left:396px;top:1182px"><svg width="26" height="26" viewBox="0 0 26 26"><path d="M7 4h12v5a6 6 0 0 1-12 0z" fill="#fff"/><path d="M7 6H3v2a4 4 0 0 0 4 4M19 6h4v2a4 4 0 0 1-4 4" stroke="#fff" stroke-width="2" fill="none"/><rect x="11.5" y="14" width="3" height="5" fill="#fff"/><rect x="8" y="19" width="10" height="3" rx="1" fill="#fff"/></svg></div>
  <div class="service left" style="left:80px;top:1322px"><h3>CUSTOM FOOD</h3><p>It is a long established fact that a reader<br>will be distracted by the readable</p></div>
  <div class="svc-icon" style="left:396px;top:1326px"><svg width="26" height="26" viewBox="0 0 26 26"><path d="M13 3c-4 0-6 3-6 6 0 4 6 13 6 13s6-9 6-13c0-3-2-6-6-6z" fill="#fff"/><circle cx="13" cy="9" r="2.4" fill="var(--magenta)"/></svg></div>
  <div class="service left" style="left:80px;top:1460px"><h3>BUS SERVICES</h3><p>It is a long established fact that a reader<br>will be distracted by the readable</p></div>
  <div class="svc-icon" style="left:396px;top:1464px"><svg width="28" height="26" viewBox="0 0 28 26"><path d="M5 12l3-6h12l3 6v7H5z" fill="#fff"/><rect x="9" y="8" width="10" height="4" fill="var(--magenta)"/><circle cx="9" cy="19" r="2.5" fill="#fff" stroke="var(--magenta)" stroke-width="1.5"/><circle cx="19" cy="19" r="2.5" fill="#fff" stroke="var(--magenta)" stroke-width="1.5"/></svg></div>

  <div class="svc-icon" style="left:735px;top:1182px"><svg width="26" height="26" viewBox="0 0 26 26"><rect x="4" y="4" width="18" height="18" rx="2" fill="none" stroke="#fff" stroke-width="2"/><path d="M8 4v18M18 4v18M4 9h4M4 13h4M4 17h4M18 9h4M18 13h4M18 17h4" stroke="#fff" stroke-width="1.6"/></svg></div>
  <div class="service" style="left:810px;top:1178px"><h3>MUSIC CLASS</h3><p>It is a long established fact that a reader<br>will be distracted by the readable</p></div>
  <div class="svc-icon" style="left:795px;top:1326px"><svg width="26" height="26" viewBox="0 0 26 26"><circle cx="13" cy="8" r="4.5" fill="#fff"/><path d="M4 22c0-5 4-8 9-8s9 3 9 8z" fill="#fff"/></svg></div>
  <div class="service" style="left:874px;top:1322px"><h3>YOGA CLASS</h3><p>It is a long established fact that a reader<br>will be distracted by the readable</p></div>
  <div class="svc-icon" style="left:735px;top:1464px"><svg width="26" height="26" viewBox="0 0 26 26"><path d="M20 4l2 2-9 10-2-2z" fill="#fff"/><path d="M10 15l2 2c-1 4-4 5-8 5 2-2 1-6 6-7z" fill="#fff"/></svg></div>
  <div class="service" style="left:810px;top:1460px"><h3>PAINTING COMPETITION</h3><p>It is a long established fact that a reader<br>will be distracted by the readable</p></div>
</section>

<section class="learning" role="img" aria-label="Dim photo of children learning together">
  <h2 class="section-title hand" style="top:62px;color:#fff;font-style:italic">LET THE LEARNING BEGIN</h2>
  <p>There are many variations of passages of Lorem Ipsum available, but the majority have suffered alteration in some form, by injected humour, or randomised words which don't look even slightly believable. If you are going to use a passage</p>
  <div class="btn" style="left:531px;top:224px;width:138px;height:44px;">JOIN NOW!</div>
</section>

<section>
  <h2 class="section-title hand services-title" style="top:2063px">OUR NEW PRICE LIST</h2>

  <div class="price-card" style="left:101px">
    <div class="price-head"><svg width="235" height="140"><path d="M0 0H235V112L0 136Z" fill="var(--magenta)"/></svg><h3 class="hand">HALF DAY</h3><small>8AM-1PM OR 1PM-6PM</small></div>
    <ul class="perks"><li><svg width="12" height="12"><path d="M2 6l3 3 5-6" stroke="var(--green)" stroke-width="2" fill="none"/></svg>Nutbreakfast</li><li><svg width="12" height="12"><path d="M2 6l3 3 5-6" stroke="var(--green)" stroke-width="2" fill="none"/></svg>snack for each session</li></ul>
    <span class="age" style="left:38px">Under 2's</span><span class="age" style="left:152px">2-5's</span>
    <div class="pill" style="left:34px">£26</div><div class="pill" style="left:134px">£25</div>
    <div class="view">VIEW DETAILS</div>
  </div>
  <div class="price-card" style="left:354px">
    <div class="price-head"><svg width="235" height="140"><path d="M0 0H235V112L0 136Z" fill="var(--magenta)"/></svg><h3 class="hand">FULL DAY</h3><small>(7.30-6PM)</small></div>
    <ul class="perks"><li><svg width="12" height="12"><path d="M2 6l3 3 5-6" stroke="var(--green)" stroke-width="2" fill="none"/></svg>Wet Breakfast</li><li><svg width="12" height="12"><path d="M2 6l3 3 5-6" stroke="var(--green)" stroke-width="2" fill="none"/></svg>snack for each session</li></ul>
    <span class="age" style="left:38px">Under 2's</span><span class="age" style="left:152px">2-5's</span>
    <div class="pill" style="left:34px">£40</div><div class="pill" style="left:134px">£38</div>
    <div class="view">VIEW DETAILS</div>
  </div>
  <div class="price-card" style="left:607px">
    <div class="price-head"><svg width="235" height="140"><path d="M0 0H235V112L0 136Z" fill="var(--magenta)"/></svg><h3 class="hand">FULL TIME</h3><small>MON- FRI: 7.30-6PM</small></div>
    <ul class="perks"><li><svg width="12" height="12"><path d="M2 6l3 3 5-6" stroke="var(--green)" stroke-width="2" fill="none"/></svg>Wet Breakfast</li><li><svg width="12" height="12"><path d="M2 6l3 3 5-6" stroke="var(--green)" stroke-width="2" fill="none"/></svg>snack for each session</li></ul>
    <span class="age" style="left:38px">Under 2's</span><span class="age" style="left:152px">2-5's</span>
    <div class="pill" style="left:34px">£168</div><div class="pill" style="left:134px">£161</div>
    <div class="view">VIEW DETAILS</div>
  </div>
  <div class="price-card" style="left:860px">
    <div class="price-head"><svg width="235" height="140"><path d="M0 0H235V112L0 136Z" fill="var(--magenta)"/></svg><h3 class="hand">FULL TIME</h3></div>
    <ul class="perks"><li><svg width="12" height="12"><path d="M2 6l3 3 5-6" stroke="var(--green)" stroke-width="2" fill="none"/></svg>Wet Breakfast</li><li><svg width="12" height="12"><path d="M2 6l3 3 5-6" stroke="var(--green)" stroke-width="2" fill="none"/></svg>snack for each session</li></ul>
    <span class="age" style="left:38px">Under 2's</span><span class="age" style="left:152px">2-5's</span>
    <div class="pill" style="left:34px">• • •</div><div class="pill" style="left:134px">£130</div>
    <div class="view">VIEW DETAILS</div>
  </div>
</section>

<section class="day">
  <div class="day-image" role="img" aria-label="Photo of two toddlers playing with colourful building blocks"></div>
  <h2 class="hand">DESCRIPTION OF OUR DAY</h2>
  <p>There are many variations of passages of Lorem Ipsum available, but the majority have suffered alteration in some form, by injected humour, or randomised words which don't look even slightly believable.</p>
  <div class="btn" style="left:98px;top:222px;width:136px;height:46px;">LEARN MORE</div>
</section>

<section>
  <h2 class="section-title hand services-title" style="top:3027px">MEET OUR TEACHER</h2>
  <p class="subtitle" style="top:3078px">Our core team was built on experience, skills and attitude and effectiveness.</p>
  <svg class="side-arrow" style="left:30px" width="24" height="30"><path d="M18 4L6 15l12 11" stroke="#888" stroke-width="4" fill="none"/></svg>
  <svg class="side-arrow" style="left:1150px" width="24" height="30"><path d="M6 4l12 11L6 26" stroke="#888" stroke-width="4" fill="none"/></svg>

  <div class="teacher" style="left:101px"><div class="photo" role="img" aria-label="Portrait photo of a smiling teacher in a classroom" style="background:linear-gradient(160deg,#c58a5a 0%,#7a4a32 45%,#2f6a5a 100%)"></div><h4>LEENA MARSH</h4><p class="role">Drawing Teacher</p><div class="socials"><span><svg width="12" height="12"><path d="M2 1l8 5-8 5z" fill="var(--magenta)"/></svg></span><span><svg width="12" height="12"><rect x="1" y="2.5" width="10" height="7" fill="none" stroke="var(--magenta)" stroke-width="1.4"/><path d="M1 3l5 4 5-4" stroke="var(--magenta)" stroke-width="1.4" fill="none"/></svg></span><span><svg width="12" height="12"><path d="M6 1v10M1 6h10" stroke="var(--magenta)" stroke-width="1.8"/></svg></span><span><svg width="12" height="12"><circle cx="6" cy="6" r="4.5" fill="none" stroke="var(--magenta)" stroke-width="1.4"/><path d="M1.5 6h9M6 1.5c-2 2.5-2 6.5 0 9M6 1.5c2 2.5 2 6.5 0 9" stroke="var(--magenta)" stroke-width="1" fill="none"/></svg></span></div></div>
  <div class="teacher" style="left:354px"><div class="photo" role="img" aria-label="Portrait photo of a teacher in a dark suit" style="background:linear-gradient(160deg,#9db4d8 0%,#4d6aa0 45%,#1a2744 100%)"></div><h4>LEENA MARSH</h4><p class="role">Drawing Teacher</p><div class="socials"><span><svg width="12" height="12"><path d="M2 1l8 5-8 5z" fill="var(--magenta)"/></svg></span><span><svg width="12" height="12"><rect x="1" y="2.5" width="10" height="7" fill="none" stroke="var(--magenta)" stroke-width="1.4"/><path d="M1 3l5 4 5-4" stroke="var(--magenta)" stroke-width="1.4" fill="none"/></svg></span><span><svg width="12" height="12"><path d="M6 1v10M1 6h10" stroke="var(--magenta)" stroke-width="1.8"/></svg></span><span><svg width="12" height="12"><circle cx="6" cy="6" r="4.5" fill="none" stroke="var(--magenta)" stroke-width="1.4"/><path d="M1.5 6h9M6 1.5c-2 2.5-2 6.5 0 9M6 1.5c2 2.5 2 6.5 0 9" stroke="var(--magenta)" stroke-width="1" fill="none"/></svg></span></div></div>
  <div class="teacher" style="left:607px"><div class="photo" role="img" aria-label="Portrait photo of a teacher holding a blue folder" style="background:linear-gradient(160deg,#a65a3a 0%,#d9a57a 45%,#3a58b0 100%)"></div><h4>LEENA MARSH</h4><p class="role">Drawing Teacher</p><div class="socials"><span><svg width="12" height="12"><path d="M2 1l8 5-8 5z" fill="var(--magenta)"/></svg></span><span><svg width="12" height="12"><rect x="1" y="2.5" width="10" height="7" fill="none" stroke="var(--magenta)" stroke-width="1.4"/><path d="M1 3l5 4 5-4" stroke="var(--magenta)" stroke-width="1.4" fill="none"/></svg></span><span><svg width="12" height="12"><path d="M6 1v10M1 6h10" stroke="var(--magenta)" stroke-width="1.8"/></svg></span><span><svg width="12" height="12"><circle cx="6" cy="6" r="4.5" fill="none" stroke="var(--magenta)" stroke-width="1.4"/><path d="M1.5 6h9M6 1.5c-2 2.5-2 6.5 0 9M6 1.5c2 2.5 2 6.5 0 9" stroke="var(--magenta)" stroke-width="1" fill="none"/></svg></span></div></div>
  <div class="teacher" style="left:860px"><div class="photo" role="img" aria-label="Portrait photo of a teacher in a green shirt" style="background:linear-gradient(160deg,#d8c9a8 0%,#b08a6a 45%,#4f7a4a 100%)"></div><h4>LEENA MARSH</h4><p class="role">Drawing Teacher</p><div class="socials"><span><svg width="12" height="12"><path d="M2 1l8 5-8 5z" fill="var(--magenta)"/></svg></span><span><svg width="12" height="12"><rect x="1" y="2.5" width="10" height="7" fill="none" stroke="var(--magenta)" stroke-width="1.4"/><path d="M1 3l5 4 5-4" stroke="var(--magenta)" stroke-width="1.4" fill="none"/></svg></span><span><svg width="12" height="12"><path d="M6 1v10M1 6h10" stroke="var(--magenta)" stroke-width="1.8"/></svg></span><span><svg width="12" height="12"><circle cx="6" cy="6" r="4.5" fill="none" stroke="var(--magenta)" stroke-width="1.4"/><path d="M1.5 6h9M6 1.5c-2 2.5-2 6.5 0 9M6 1.5c2 2.5 2 6.5 0 9" stroke="var(--magenta)" stroke-width="1" fill="none"/></svg></span></div></div>
</section>

<section class="accred">
  <svg class="abs" style="left:90px;top:0" width="1020" height="363" aria-hidden="true"><path d="M10 20l30 30M60 10h40M980 40a30 30 0 1 0 30 30M880 330l20-30 10 20" stroke="#e2e2e2" stroke-width="6" fill="none"/></svg>
  <h2 class="section-title hand services-title" style="top:62px">TRAINING ACCREDITATION'S</h2>
  <p class="subtitle" style="top:112px;font-size:12.5px">There are many variations of passages of Lorem Ipsum available, but the majority have suffered alteration</p>
  <div class="badge-box" style="left:101px"><svg width="130" height="60"><path d="M45 8h40v22l-20 22-20-22z" fill="#2b2b2b"/><rect x="20" y="52" width="90" height="4" fill="#b7b7b7"/></svg></div>
  <div class="badge-box" style="left:306px"><svg width="130" height="60"><rect x="10" y="6" width="110" height="26" fill="#3a3a3a"/><rect x="10" y="38" width="110" height="14" fill="#8a8a8a"/></svg></div>
  <div class="badge-box" style="left:506px"><svg width="130" height="60"><circle cx="28" cy="30" r="20" fill="#555"/><rect x="56" y="18" width="66" height="12" fill="#2b2b2b"/><rect x="56" y="36" width="50" height="6" fill="#aaa"/></svg></div>
  <div class="badge-box" style="left:709px"><svg width="130" height="60"><rect x="14" y="10" width="102" height="30" rx="4" fill="#333"/><rect x="14" y="46" width="102" height="6" fill="#b0b0b0"/></svg></div>
  <div class="badge-box" style="left:914px"><svg width="130" height="60"><circle cx="28" cy="26" r="18" fill="#444"/><rect x="52" y="12" width="70" height="26" fill="#2b2b2b"/><rect x="12" y="48" width="110" height="5" fill="#aaa"/></svg></div>
</section>

<footer class="footer">
  <h5 style="left:98px">CONTACT DETAILS</h5>
  <h5 style="left:417px">JOIN OUR NEWSLETTER</h5>
  <h5 style="left:747px">CHATTERLY FEED</h5>
  <div class="abs" style="left:1080px;top:84px;width:20px;height:20px;background:#3b5bd0"></div>

  <div class="contact-item" style="top:134px"><span class="ic"><svg width="16" height="18"><path d="M8 1c-3 0-5 2-5 5 0 3.5 5 11 5 11s5-7.5 5-11c0-3-2-5-5-5z" fill="#fff"/><circle cx="8" cy="6" r="2" fill="#121212"/></svg></span><span>48 Orchard Lane, Fernbridge,<br>Westshire</span></div>
  <div class="contact-item" style="top:195px"><span class="ic"><svg width="16" height="16"><path d="M3 1l3 1 1 4-2 1c1 2 2 3 4 4l1-2 4 1 1 3-2 2C7 15 1 9 1 3z" fill="#fff"/></svg></span><span>(+1) 555 014 2290</span></div>
  <div class="contact-item" style="top:255px"><span class="ic"><svg width="16" height="12"><rect x="0.5" y="0.5" width="15" height="11" fill="#fff"/><path d="M1 1l7 6 7-6" stroke="#121212" stroke-width="1.4" fill="none"/></svg></span><span>hello@brightacornsnursery.example</span></div>
  <div class="contact-item" style="top:314px"><span class="ic"><svg width="16" height="16"><circle cx="8" cy="8" r="7" fill="none" stroke="#fff" stroke-width="1.6"/><path d="M8 4v4l3 2" stroke="#fff" stroke-width="1.6" fill="none"/></svg></span><span>Mon - Sat: 7:30 - 6pm</span></div>

  <div class="news-input">Enter Your Email</div>
  <div class="subscribe">SUBSCRIBE</div>
  <div class="seal" style="left:417px;top:238px;width:90px;height:78px;background:#2a3f8a"></div>
  <div class="seal" style="left:523px;top:238px;width:90px;height:78px;background:#2a3f8a"></div>
  <div class="seal" style="left:417px;top:328px;width:146px;height:60px;background:#fff"></div>

  <div class="feed">
    <div class="feed-banner" role="img" aria-label="Cover photo of the nursery chatterly page">
      <div class="feed-logo"></div>
      <b>BRIGHT ACORNS DAY NURSERY</b>
      <small>322 Likes</small>
    </div>
    <p class="abs" style="left:14px;top:126px;font-size:11px">You and 8 other friends like this</p>
    <div class="abs" role="img" aria-label="Row of friend profile photos" style="left:14px;top:150px;width:324px;height:60px;background:linear-gradient(90deg,#8aa0c0,#c7b7a6,#8aa0c0,#b8a0a0)"></div>
  </div>
</footer>

<div class="bottom-bar">
  <p class="abs" style="left:0;width:1200px;top:38px;text-align:center">© Copyright 2017 · Bright Acorns Day Nursery. All Rights Reserved &nbsp;&nbsp;&nbsp;|&nbsp;&nbsp;&nbsp; Privacy Policy</p>
</div>

</body>
</html>
```